Corvane Alloys Collective Business Card

Design a business card for a new company. Corvane Alloys Collective is a subsidiary of KTP, Inc. (www.ktpreclaims.example)

Target Market(s)

B2B, Manufactures

Industry/Entity Type

Recycling

Contact Information for Business Card

Corvane Alloys Collective, LLC.
48217 North Wendlow Avenue
Marrowfield OH 44871
P: (312) 555-0143
F: (312) 555-0144
www.corvaneac.example
Email@corvaneac.example

Font styles to use
Sans Serif

Requirements
Must have
• A KTP, Inc. subsidiary company.
Nice to have
• Reclaimed Metals. Reliably Delivered. (slogan)

```html
<!DOCTYPE html>
<html lang="en">
<head>
<meta charset="utf-8">
<title>Corvane Alloys Collective Business Card</title>
<link rel="stylesheet" href="https://fonts.googleapis.com/css2?family=Open+Sans:wght@400;600;700&display=swap">
<style>
  :root {
    --bg: #ecebe6;
    --green-light: #6ea93c;
    --green-dark: #215c2d;
    --green-mid: #3f8a35;
    --blue: #1d4fa6;
    --white: #ffffff;
    --shadow: rgba(0, 0, 0, 0.18);
  }
  * { box-sizing: border-box; margin: 0; padding: 0; }
  html, body {
    width: 1200px; height: 1022px; overflow: hidden;
    background: var(--bg);
    font-family: "Open Sans", Arial, sans-serif;
  }
  .canvas { position: relative; width: 1200px; height: 1022px; }
  .card {
    position: absolute;
    width: 560px; height: 320px;
    border-radius: 22px;
    overflow: hidden;
    box-shadow: 0 10px 28px var(--shadow);
  }
  .card-front { left: 320px; top: 110px; background: var(--white); }
  .card-front .panel { position: absolute; inset: 0; width: 100%; height: 100%; }
  .brand-front {
    position: absolute; left: 28px; top: 128px; width: 220px;
    display: flex; align-items: center; gap: 10px;
    color: var(--green-dark); font-weight: 700; font-size: 21px; line-height: 1.15;
  }
  .brand-mark {
    flex: none; width: 26px; height: 26px; border-radius: 50%;
    background: var(--green-mid);
  }
  .person { position: absolute; left: 318px; top: 30px; }
  .person-name { color: var(--blue); font-weight: 700; font-size: 22px; line-height: 1.1; }
  .person-title { color: var(--white); font-size: 14px; margin-top: 2px; }
  .contact-list {
    position: absolute; left: 318px; top: 106px; list-style: none;
    color: var(--white); font-size: 13px; line-height: 21px;
  }
  .contact-list li { display: flex; align-items: center; gap: 8px; }
  .contact-list svg { width: 13px; height: 13px; flex: none; }
  .address {
    position: absolute; left: 318px; top: 222px;
    color: var(--white); font-size: 13.5px; line-height: 21px; font-style: normal;
  }
  .card-back {
    left: 320px; top: 560px;
    background: linear-gradient(200deg, var(--green-light) 0%, var(--green-mid) 45%, var(--green-dark) 100%);
    color: var(--white);
  }
  .brand-back {
    position: absolute; left: 0; right: 0; top: 100px;
    display: flex; justify-content: center; align-items: center; gap: 12px;
    font-weight: 700; font-size: 28px;
  }
  .brand-back .brand-mark { background: var(--white); width: 30px; height: 30px; }
  .web-back {
    position: absolute; left: 0; right: 0; top: 170px; text-align: center;
    font-size: 13px;
  }
  .slogan {
    position: absolute; left: 0; right: 0; bottom: 36px; text-align: center;
    font-size: 20px; letter-spacing: 0.3px;
  }
</style>
</head>
<body>
<main class="canvas">
  <section class="card card-front" aria-label="Business card front">
    <svg class="panel" viewBox="0 0 560 320" preserveAspectRatio="none" aria-hidden="true">
      <defs>
        <linearGradient id="greenFront" x1="0" y1="0" x2="1" y2="1">
          <stop offset="0" stop-color="#6ea93c"/>
          <stop offset="1" stop-color="#215c2d"/>
        </linearGradient>
      </defs>
      <path d="M250 0 Q300 160 258 320 L560 320 L560 0 Z" fill="#1d4fa6"/>
      <path d="M266 0 Q316 160 274 320 L560 320 L560 0 Z" fill="url(#greenFront)"/>
    </svg>
    <div class="brand-front"><span class="brand-mark"></span><span>Corvane Alloys Collective</span></div>
    <div class="person">
      <p class="person-name">Marlo Finch</p>
      <p class="person-title">President</p>
    </div>
    <ul class="contact-list">
      <li><svg viewBox="0 0 16 16"><path d="M4 1h3l1 4-2 1a9 9 0 0 0 4 4l1-2 4 1v3c0 1-1 2-2 2C7 14 2 9 2 3c0-1 1-2 2-2z" fill="#fff"/></svg>(312) 555-0143</li>
      <li><svg viewBox="0 0 16 16"><rect x="4" y="1" width="8" height="4" fill="#fff"/><rect x="1" y="6" width="14" height="6" rx="1" fill="#fff"/><rect x="4" y="10" width="8" height="5" fill="#fff"/></svg>(312) 555-0144</li>
      <li><svg viewBox="0 0 16 16"><rect x="1" y="3" width="14" height="10" fill="none" stroke="#fff" stroke-width="1.5"/><path d="M1 3l7 6 7-6" fill="none" stroke="#fff" stroke-width="1.5"/></svg>info@corvaneac.example</li>
      <li><svg viewBox="0 0 16 16"><rect x="1" y="2" width="14" height="10" fill="none" stroke="#fff" stroke-width="1.5"/><rect x="5" y="13" width="6" height="2" fill="#fff"/></svg>www.corvaneac.example</li>
    </ul>
    <address class="address">
      A KTP, Inc. subsidiary company<br>
      48217 North Wendlow Avenue<br>
      Marrowfield OH 44871
    </address>
  </section>

  <section class="card card-back" aria-label="Business card back">
    <div class="brand-back"><span class="brand-mark"></span><span>Corvane Alloys Collective</span></div>
    <p class="web-back">www.corvaneac.example</p>
    <p class="slogan">Reclaimed Metals. Reliably Delivered</p>
  </section>
</main>
</body>
</html>
```